New Business Card/Website Logo

We need a business card design for a new company based in Sydney. The company focuses mainly in construction in the field of form work and concreting. Attached is the logo being used already which can be used as a base for a new design, the current one is simply too bland and we are looking to spruce it up so it stands out and looks nicer. The logo would also be used on the website which is currently under construction. The attached image has the name, mobile and also the license number which needs to be there. The current email address on there can be removed and can be replaced with the website http://www.bravelintel.com.au, thanks!
Updates

Target Market(s)

Construction industry. Focusing on form work and concreting

Industry/Entity Type

Construction

Requirements
Must have
• License # on card along with website http://www.bravelintel.com.au and mobile phone number
Nice to have
• You have freedom with the design. The current design was a mock up done quite quickly. Please just keep in mind the target audience - construction, thanks.
Should not have
• the mailvista email address can be removed(refer picture) and replaced somewhere on the design with the website http://www.bravelintel.com.au

```html
<!DOCTYPE html>
<html lang="en">
<head>
<meta charset="utf-8">
<title>Bravelintel – Business Card</title>
<link rel="stylesheet" href="https://fonts.googleapis.com/css2?family=Mulish:wght@700;800&family=Questrial&display=swap">
<style>
  :root {
    --page: #e9e7e3;
    --paper: #ffffff;
    --brand-green: #3aa12f;
    --ink: #0d0d0d;
    --light: #ffffff;
  }
  * { margin: 0; padding: 0; box-sizing: border-box; }
  html, body { width: 1200px; height: 900px; overflow: hidden; }
  body {
    background: var(--page);
    font-family: "Questrial", "Century Gothic", sans-serif;
  }
  .business-card {
    position: absolute;
    left: 120px; top: 170px;
    width: 960px; height: 560px;
    background: var(--paper);
    box-shadow: 0 10px 30px rgba(0,0,0,0.18);
    overflow: hidden;
  }
  .card-shapes { position: absolute; inset: 0; }
  .card-shapes .green-panel { fill: var(--brand-green); }
  .card-shapes .dark-band, .card-shapes .dark-stripe { fill: var(--ink); }

  .holder-name {
    position: absolute; left: 48px; top: 128px;
    font-family: "Mulish", "Century Gothic", sans-serif;
    font-weight: 800; font-size: 44px; letter-spacing: 1px;
    color: var(--light);
  }
  .holder-role {
    position: absolute; left: 200px; top: 186px;
    font-family: "Mulish", "Century Gothic", sans-serif;
    font-weight: 800; font-size: 24px;
    color: var(--ink);
  }
  .licence {
    position: absolute; left: 340px; top: 332px;
    font-size: 17px; font-weight: 700;
    font-family: "Mulish", "Century Gothic", sans-serif;
    color: var(--ink);
  }
  .phone {
    position: absolute; left: 30px; top: 376px;
    font-size: 17px;
    color: var(--ink);
  }
  .website {
    position: absolute; left: 0; top: 465px; width: 600px;
    text-align: center;
    font-family: "Mulish", "Century Gothic", sans-serif;
    font-weight: 700; font-size: 30px;
    color: var(--light);
  }
  .website .domain { color: var(--brand-green); }

  .brand {
    position: absolute; left: 700px; top: 220px;
    display: flex; align-items: center; gap: 18px;
  }
  .brand-square {
    width: 34px; height: 34px;
    background: var(--brand-green);
  }
  .brand-name {
    font-family: "Questrial", "Century Gothic", sans-serif;
    font-size: 44px;
    color: var(--ink);
  }
</style>
</head>
<body>
  <main class="business-card">
    <svg class="card-shapes" width="960" height="560" viewBox="0 0 960 560" aria-hidden="true">
      <polygon class="green-panel" points="0,0 500,0 590,400 0,400"/>
      <polygon class="dark-stripe" points="525,0 547,0 673,560 651,560"/>
      <polygon class="dark-band" points="0,415 640,415 673,560 0,560"/>
    </svg>

    <h1 class="holder-name">MATEO ALVAREZ</h1>
    <p class="holder-role">Director General</p>
    <p class="licence">Licence: 384512C</p>
    <p class="phone">Phone: 04 12 555 078</p>
    <p class="website">www.<span class="domain">bravelintel</span>.com.au</p>

    <div class="brand">
      <span class="brand-square"></span>
      <span class="brand-name">Bravelintel</span>
    </div>
  </main>
</body>
</html>
```